Pelvin Advisory Business Card Design

Business card for business consulting company, using attached logo. We do financial and strategic consulting, and want a clean, professional image with a bit of fun. Our logo is a flat whale tail, which symbolizes the Orca whale, a highly collaborative, group based animal that is very successful in navigating the ocean, protecting the herd, and hunting. We like the logo that is blue and gray on white one one side, but would be open to a blue card with white lettering on the other side... or whatever you'd suggest
Updates
Hi all - I have had the logo modified to take the shadowing off the tail. I will post it on the brief... under a file name called updated logo. thank you Added Saturday, April 25, 2015
Target Market(s)
Small to medium sized businesses ($10M to $500M in revenue per year), financial and sales executives, general managers, attorneys and CPAs
Industry/Entity Type
Financial
Contact Information for Business Card
Want company name, contact info - name, title, telephone, email, website, linkedin, twitter and Facebook. No physical address yet.
Requirements
Must have
- contemporary design, bold, strong, confident but with a bit of fun. prominently feature the logo and the whale tail icon
Nice to have
- unique touches that would differentiate us from a regular card... for example, logo and writing all on front on white background, but on back - logo in white on a blue background
- open to idea of different shapes of card than standard... but not sure

```html
<!DOCTYPE html>
<html lang="en">
<head>
<meta charset="utf-8">
<title>Pelvin Advisory Business Card</title>
<link href="https://fonts.googleapis.com/css2?family=Montserrat:wght@400;600&display=swap" rel="stylesheet">
<style>
  :root {
    --navy: #0f3a73;
    --grey-band: #b9bbbe;
    --grey-text: #8a8d91;
    --card-white: #fbfbfb;
    --stage: #e7e8ea;
    --white: #ffffff;
  }
  html, body {
    margin: 0;
    padding: 0;
    width: 1200px;
    height: 828px;
    overflow: hidden;
    background: var(--stage);
    font-family: "Montserrat", Arial, sans-serif;
  }
  .canvas {
    position: relative;
    width: 1200px;
    height: 828px;
  }
  .card {
    position: absolute;
    top: 260px;
    width: 540px;
    height: 309px;
    background: linear-gradient(160deg, var(--white) 0%, var(--card-white) 60%, #f0f0f1 100%);
    box-shadow: 0 6px 18px rgba(0,0,0,0.12), 0 1px 3px rgba(0,0,0,0.1);
    overflow: hidden;
  }
  .card--front { left: 40px; }
  .card--back { left: 620px; }

  .brand {
    position: absolute;
    display: flex;
    align-items: center;
    gap: 14px;
  }
  .card--front .brand {
    left: 50%;
    top: 50%;
    transform: translate(-50%, -50%);
  }
  .card--back .brand {
    left: 130px;
    top: 70px;
  }
  .brand__square {
    width: 46px;
    height: 46px;
    border-radius: 8px;
    background: var(--navy);
    flex: none;
  }
  .card--back .brand__square {
    width: 38px;
    height: 38px;
    border-radius: 7px;
  }
  .brand__name {
    font-weight: 600;
    font-size: 30px;
    letter-spacing: -0.5px;
    color: var(--navy);
    white-space: nowrap;
  }
  .card--back .brand__name { font-size: 25px; }

  .back-art {
    position: absolute;
    inset: 0;
    width: 100%;
    height: 100%;
  }
  .person {
    position: absolute;
    left: 30px;
    bottom: 34px;
    color: var(--white);
  }
  .person__name {
    font-size: 15px;
    font-weight: 400;
    letter-spacing: 1px;
    text-transform: uppercase;
  }
  .person__title {
    font-size: 11px;
    letter-spacing: 1px;
    text-transform: uppercase;
    margin-top: 3px;
  }
  .contact {
    position: absolute;
    right: 26px;
    top: 198px;
    display: grid;
    grid-template-columns: auto auto;
    column-gap: 22px;
    row-gap: 6px;
    color: var(--white);
    font-size: 10px;
    line-height: 1.35;
  }
  .contact__address {
    grid-column: 1 / 3;
    font-size: 11px;
    margin-bottom: 6px;
  }
  .contact__item {
    display: flex;
    align-items: center;
    gap: 6px;
    white-space: nowrap;
  }
  .contact__icon {
    width: 11px;
    height: 11px;
    flex: none;
    fill: none;
    stroke: var(--white);
    stroke-width: 1.6;
    stroke-linecap: round;
    stroke-linejoin: round;
  }
</style>
</head>
<body>
<main class="canvas">

  <section class="card card--front" aria-label="Card front">
    <div class="brand">
      <span class="brand__square"></span>
      <span class="brand__name">Pelvin Advisory</span>
    </div>
  </section>

  <section class="card card--back" aria-label="Card back">
    <svg class="back-art" viewBox="0 0 540 309" preserveAspectRatio="none" aria-hidden="true">
      <path d="M0,198 C210,198 390,150 540,18 L540,309 L0,309 Z" fill="var(--grey-band)"/>
      <path d="M0,212 C215,212 395,166 540,40 L540,309 L0,309 Z" fill="var(--navy)"/>
    </svg>

    <div class="brand">
      <span class="brand__square"></span>
      <span class="brand__name">Pelvin Advisory</span>
    </div>

    <div class="person">
      <div class="person__name">Dana Whitcombe</div>
      <div class="person__title">President</div>
    </div>

    <div class="contact">
      <div class="contact__address">Suite 4, Harbour House<br>Quay Road North</div>
      <div class="contact__item">
        <svg class="contact__icon" viewBox="0 0 12 12"><path d="M3 1 L5 3.5 L4 5 Q5.5 7 7 8 L8.5 7 L11 9 L10 11 Q5 11 1 5 Q1 2 3 1 Z"/></svg>
        020 7946 0418
      </div>
      <div class="contact__item">
        <svg class="contact__icon" viewBox="0 0 12 12"><rect x="1" y="2.5" width="10" height="7" rx="1"/><path d="M1 3 L6 7 L11 3"/></svg>
        dana@pelvinadvisory.com
      </div>
      <div class="contact__item">
        <svg class="contact__icon" viewBox="0 0 12 12"><rect x="3" y="1" width="6" height="10" rx="1"/><path d="M5.5 9.3 L6.5 9.3"/></svg>
        020 7946 0419
      </div>
      <div class="contact__item">
        <svg class="contact__icon" viewBox="0 0 12 12"><circle cx="6" cy="6" r="5"/><path d="M1 6 L11 6 M6 1 Q3 6 6 11 M6 1 Q9 6 6 11"/></svg>
        www.pelvinadvisory.com
      </div>
    </div>
  </section>

</main>
</body>
</html>
```